Construction company focused on concrete and shed construction.

We need to update our current business card for ridgeforgebuilds.com.au we would like an eye catching design with blue, grey and white incorporating our current logo.
Our company started off in concreting and due to varying factors we have expanded to include shed construction as well.
This has led to our current Logo looking a little out of place and somehow need to use the card to bring in the shed construction side of the business while not having to change current concrete look "KESTRO" logo as we already have this incorporated into our company clothing and are not willing to change this yet.
Photo image attached for inspiration/ visual reference of type of work, not to be used on final design.
Please no cheesy designs of men in hard hats and tools
Final design should demonstrate a modern and service focused company.

Target Market(s)

Farmers, Business owners, Developers, Architects, Commercial project delivery

Industry/Entity Type

Construction Company

Contact Information for Business Card

Kestro Constructions.
7b Harlow st
South Launceston Tas
03 62918873

Font styles to use
Other font styles liked:
• see font in logo

Colors
3176b5
b2b2b2

Requirements
Must have
• Easy to read font,
• good contrast between back ground and writing
Nice to have
• Modern and corporate look with a fun but professional image.
Should not have
• Comic images or shadow images of tools/ people.

```html
<!DOCTYPE html>
<html lang="en">
<head>
<meta charset="utf-8">
<title>Kestro Constructions – Business Card</title>
<link href="https://fonts.googleapis.com/css2?family=Josefin+Sans:wght@400;600;700&display=swap" rel="stylesheet">
<style>
  :root {
    --brand-blue: #1f66ad;
    --slate: #3a4347;
    --mid-grey: #8f9294;
    --concrete: #dcdcda;
    --concrete-dark: #c6c6c3;
    --white: #ffffff;
    --stage: #ecebe8;
  }
  * { box-sizing: border-box; margin: 0; padding: 0; }
  html, body {
    width: 1200px; height: 800px; overflow: hidden;
    background: var(--stage);
    font-family: "Josefin Sans", sans-serif;
  }
  .stage {
    position: relative; width: 1200px; height: 800px;
  }
  .card {
    position: absolute; top: 252px;
    width: 520px; height: 297px;
    overflow: hidden;
    box-shadow: 0 6px 18px rgba(0,0,0,0.18);
  }
  .card--front { left: 50px; }
  .card--back {
    left: 630px;
    background: radial-gradient(ellipse at 30% 30%, var(--concrete) 0%, var(--concrete-dark) 100%);
  }
  .card__bg { position: absolute; inset: 0; }
  .brand-seal {
    position: absolute;
    width: 170px; height: 170px; border-radius: 50%;
    background: var(--white);
    display: flex; align-items: center; justify-content: center;
    color: var(--brand-blue);
    font-weight: 700; font-size: 34px; letter-spacing: 2px;
    padding-top: 6px;
  }
  .card--front .brand-seal { left: 100px; top: 56px; }
  .card--back .brand-seal { left: 175px; top: 63px; }
  .contact {
    position: absolute; left: 272px; top: 58px;
    color: var(--white);
  }
  .contact__name { font-size: 25px; font-weight: 600; letter-spacing: 1px; }
  .contact__role { font-size: 11px; letter-spacing: 1.5px; margin-top: 4px; }
  .contact__company { font-size: 15px; letter-spacing: 1px; margin-top: 16px; }
  .contact__line {
    display: flex; align-items: flex-start; gap: 10px;
    font-size: 12.5px; letter-spacing: 1px; line-height: 1.35;
    margin-top: 14px;
  }
  .contact__icon { width: 14px; height: 14px; flex: none; margin-top: 1px; }
</style>
</head>
<body>
<main class="stage">
  <section class="card card--front" aria-label="Business card front">
    <svg class="card__bg" viewBox="0 0 520 297" width="520" height="297" aria-hidden="true">
      <rect width="520" height="297" fill="var(--brand-blue)"/>
      <rect width="185" height="297" fill="var(--slate)"/>
      <polygon points="185,170 345,297 185,297" fill="var(--mid-grey)"/>
    </svg>
    <div class="brand-seal">KESTRO</div>
    <div class="contact">
      <p class="contact__name">LOREM IPSUM</p>
      <p class="contact__role">MANAGER</p>
      <p class="contact__company">KESTRO CONSTRUCTIONS</p>
      <p class="contact__line">
        <svg class="contact__icon" viewBox="0 0 14 14" aria-hidden="true"><path d="M7 1 L1 7 H3 V13 H6 V9 H8 V13 H11 V7 H13 Z" fill="var(--white)"/></svg>
        <span>7B HARLOW ST<br>SOUTH LAUNCESTON TAS</span>
      </p>
      <p class="contact__line">
        <svg class="contact__icon" viewBox="0 0 14 14" aria-hidden="true"><path d="M3 1 L5.5 1 L6.5 4 L5 5.5 C5.8 7.3 6.7 8.2 8.5 9 L10 7.5 L13 8.5 L13 11 C13 12 12 13 11 13 C6 13 1 8 1 3 C1 2 2 1 3 1 Z" fill="var(--white)"/></svg>
        <span>03 62918873</span>
      </p>
    </div>
  </section>

  <section class="card card--back" aria-label="Business card back">
    <div class="brand-seal">KESTRO</div>
  </section>
</main>
</body>
</html>
```